Digitale Weihnachtskarte für Energieberater
Zielgruppe
Beratung in Bezug auf Energiemanagement/Energieeffizienz in Gebäuden
Gebäudetechnik
Kunden aufzeigen, wie Energie und somit Kosten gespart werden können
Zielgruppe: unsere Kunden, Interessenten und Lieferanten
Aufgabenstellung
Die digitale Weihnachtskarte wird schlussendlich per Mailing verschickt. Es wird eine jpg- und eine pdf-Datei benötigt.
Design:
Weihnachtliches, eher schlichtes Design. Letztjährige Projekte: #293721, #484192, #437447
Logo muss integriert werden, muss aber nicht im Vordergrund stehen.
Das Bild im Anhang kann, aber muss nicht verwendet werden.
Farbwahl:
Blau:
CMYK = 95/75/0/0
HEX = #244a9a
RGB = 36/74/154
Orange:
CMYK = 0/60/100/0
HEX = #ef7d00
RGB = 239/125/0
Grau:
CMYK = 0/0/0/65
HEX = #7c7c7b
RGB = 124/124/123
Grün:
CMYK = 60/100/0/0
HEX = #76b82a
RGB = 118/184/42
Schrift: DIN oder Arial, nicht kursiv
Geschätzte Kunden und Partner
Das Jahr neigt sich dem Ende zu und lädt uns dazu ein, auf das vergangene Jahr zurückzublicken, aber auch mit Zuversicht und frischem Elan in einen neuen Zeitabschnitt zu starten. Dank fortschrittlichen Technologien, Prozessoptimierungen und Investitionen wurde der Erfolg der vendralis Schweiz AG vorangetrieben. Mit unserem neuen Standort in Stuttgart haben wir einen weiteren Meilenstein gelegt.
Dankbar dafür, dass wir mit Ihnen zusammen in die Zukunft weiterschreiten dürfen, wünschen wir Ihnen und Ihrer Familie eine entspannte und besinnliche Weihnachtszeit und ein glückliches neues Jahr!

```html
<!DOCTYPE html>
<html lang="de">
<head>
<meta charset="utf-8">
<title>Weihnachtskarte – vendralis Schweiz AG</title>
<link href="https://fonts.googleapis.com/css2?family=Arimo:wght@400&family=Pinyon+Script&display=swap" rel="stylesheet">
<style>
  :root {
    --page-bg: #f3f3f3;
    --brand-blue: #244a9a;
    --footer-bg: #ffffff;
    --text-light: #ffffff;
    --night-deep: #04051a;
    --night-mid: #0a1f66;
    --glow-blue: #1f74dc;
    --violet-edge: #3a1f4f;
  }
  * { box-sizing: border-box; margin: 0; padding: 0; }
  html, body {
    width: 900px; height: 1200px; overflow: hidden;
    background: var(--page-bg);
    font-family: "Arimo", Arial, sans-serif;
  }
  .card {
    position: absolute; left: 23px; top: 83px; width: 852px;
    box-shadow: 0 1px 4px rgba(0,0,0,0.25);
  }
  .card-header {
    position: relative; height: 441px; overflow: hidden;
    background:
      radial-gradient(ellipse 260px 200px at 455px 210px, rgba(120,200,255,0.85), rgba(31,116,220,0.55) 40%, transparent 75%),
      radial-gradient(ellipse 340px 320px at 720px 230px, rgba(40,90,200,0.55), transparent 80%),
      linear-gradient(100deg, var(--night-deep) 0%, var(--night-mid) 30%, var(--glow-blue) 52%, #0c2a78 72%, var(--violet-edge) 100%);
  }
  .greeting-word {
    position: absolute;
    font-family: "Pinyon Script", cursive;
    font-size: 30px; line-height: 1;
    color: var(--text-light);
    white-space: nowrap;
  }
  .greeting-frohes { left: 139px; top: 70px; }
  .greeting-neues { left: 241px; top: 145px; }
  .greeting-jahr { left: 70px; top: 265px; font-size: 33px; }
  .greeting-frohe { left: 292px; top: 268px; }
  .greeting-weihnachten { left: 40px; top: 385px; }
  .card-body {
    background: var(--brand-blue);
    color: var(--text-light);
    height: 442px;
    padding: 70px 30px 0 48px;
    font-size: 18.6px; line-height: 24px;
    hyphens: auto;
  }
  .card-body p + p { margin-top: 24px; }
  .card-footer {
    position: relative; height: 87px;
    background: var(--footer-bg);
    color: var(--brand-blue);
    font-size: 12px; line-height: 14.5px;
  }
  .address { position: absolute; top: 16px; }
  .address-ch { left: 46px; }
  .address-de { left: 227px; }
  .website { position: absolute; left: 477px; top: 60px; }
  .brand-name {
    position: absolute; left: 642px; top: 24px;
    display: flex; align-items: center; gap: 8px;
    font-size: 25px; line-height: 1; color: var(--brand-blue);
  }
  .brand-dot {
    width: 30px; height: 30px; border-radius: 50%;
    background: var(--brand-blue);
  }
</style>
</head>
<body>
  <article class="card">
    <header class="card-header" role="img" aria-label="Sternenbaum aus kleinen Sternen neben einer leuchtenden blauen Weltkugel aus vernetzten Lichtlinien">
      <span class="greeting-word greeting-frohes">Frohes</span>
      <span class="greeting-word greeting-neues">neues</span>
      <span class="greeting-word greeting-jahr">Jahr</span>
      <span class="greeting-word greeting-frohe">Frohe</span>
      <span class="greeting-word greeting-weihnachten">Weihnachten</span>
    </header>

    <section class="card-body">
      <p>Geschätzte Kunden und Partner</p>
      <p>Das Jahr neigt sich dem Ende zu und lädt uns dazu ein, auf das vergangene Jahr zu&shy;rückzublicken, aber auch mit Zuversicht und frischem Elan in einen neuen Zeitabschnitt zu starten. Dank fortschrittlichen Technologien, Prozessoptimierungen und Investitionen wurde der Erfolg der vendralis Schweiz AG vorangetrieben. Mit unserem neuen Stan&shy;dort in Stuttgart haben wir einen weiteren Meilenstein gelegt.</p>
      <p>Dankbar dafür, dass wir mit Ihnen zusammen in die Zukunft weiterschreiten dürfen, wünschen wir Ihnen und Ihrer Familie eine entspannte und besinnliche Weihnachtszeit und ein glückliches neues Jahr!</p>
      <p>Ihr vendralis-Team</p>
    </section>

    <footer class="card-footer">
      <address class="address address-ch" style="font-style:normal">
        vendralis Schweiz AG<br>
        Lindenweg 12<br>
        4600 Olten<br>
        Tel. +41 62 000 12 34
      </address>
      <address class="address address-de" style="font-style:normal">
        vendralis Schweiz AG<br>
        Niederlassung Deutschland<br>
        Werkstrasse 9, 70565 Stuttgart<br>
        Tel. +49 711 000 45 60
      </address>
      <span class="website">www.vendralis.example</span>
      <div class="brand-name"><span>vendralis</span><span class="brand-dot"></span></div>
    </footer>
  </article>
</body>
</html>
```